It's a new electrical company based in Newcastle NSW. I would like a logo between the two words "BRANO (insert logo) VOLT". I would like the logo to represent electrical and celtic style. For example I have seen a light bulb with a celtic pattern in the middle which looked very good. I would like it to be a white card, mainly black writing and quite basic not too much going on. But maybe have the logo partially red or green?

Reason: Waiting for new e mail address so I can put it on the business card

Industry/Entity Type

Electrical

Contact Information for Business Card

BRANO VOLT
Electrical Contractors
Domestic, commercial, fault finding, testing, re wires, switchboard upgrades
License No: 730482K
Fully Insured
Phone: 0487310294

```html
<!DOCTYPE html>
<html lang="en">
<head>
<meta charset="utf-8">
<title>BRANO VOLT – Electrical Contractors</title>
<link rel="stylesheet" href="https://fonts.googleapis.com/css2?family=Montserrat:ital,wght@0,300;0,400;0,700;1,400;1,700&display=swap">
<style>
  :root {
    --card-bg: #1b1f20;
    --ink-white: #ffffff;
    --accent-cyan: #4fd6fb;
  }
  html, body {
    margin: 0;
    padding: 0;
    overflow: hidden;
    background: var(--card-bg);
  }
  .card {
    position: relative;
    width: 693px;
    height: 1200px;
    background: var(--card-bg);
    overflow: hidden;
    font-family: "Montserrat", sans-serif;
    color: var(--ink-white);
  }
  .brand {
    position: absolute;
    top: 345px;
    left: 0;
    width: 693px;
    display: flex;
    justify-content: center;
    align-items: center;
    gap: 16px;
  }
  .brand-word {
    font-weight: 700;
    font-size: 84px;
    line-height: 1;
    letter-spacing: 2px;
    color: var(--ink-white);
  }
  .brand-dot {
    width: 82px;
    height: 82px;
    border-radius: 50%;
    background: var(--accent-cyan);
    flex: none;
  }
  .tagline {
    position: absolute;
    top: 446px;
    left: 0;
    width: 693px;
    text-align: center;
    font-weight: 300;
    font-size: 35px;
    letter-spacing: 8.5px;
    color: var(--accent-cyan);
    line-height: 1;
  }
  .details {
    position: absolute;
    left: 55px;
    top: 866px;
    font-size: 30px;
    font-weight: 300;
    line-height: 39.5px;
  }
  .details p { margin: 0; }
  .insured {
    font-weight: 700;
    font-style: italic;
  }
  .services {
    margin: 4px 0 0;
    font-style: italic;
    font-weight: 400;
    font-size: 25.5px;
    line-height: 34px;
    color: var(--accent-cyan);
  }
  .corner-circle {
    position: absolute;
    left: 434px;
    top: 948px;
  }
</style>
</head>
<body>
  <main class="card">
    <div class="brand">
      <span class="brand-word">BRANO</span>
      <span class="brand-dot" aria-hidden="true"></span>
      <span class="brand-word">VOLT</span>
    </div>
    <div class="tagline">Electrical Contractors</div>

    <section class="details">
      <p>License No: 730482K</p>
      <p>Phone: 0487310294</p>
      <p class="insured">Fully Insured</p>
      <p class="services">Domestic,<br>Commercial,<br>Fault Finding,<br>Testing, Rewires,<br>Switchboard Upgrades</p>
    </section>

    <svg class="corner-circle" width="328" height="328" viewBox="0 0 328 328" aria-hidden="true">
      <circle cx="164" cy="164" r="164" fill="var(--accent-cyan)"/>
    </svg>
  </main>
</body>
</html>
```